Modern Ebook Design: The Spy's Guide to Marketing: Small Business Marketing Lessons from the BRX

I need to convert a document I've written into an ebook for my marketing company, Blue Anchor Partners. The ebook, as mentioned, is about lessons I learned as a BRX officer that can be used for small business marketing. The title I'm thinking of right now "The Spy's Guide to Marketing: Secrets for Small Business Marketing from the BRX" (but I'm open to other suggestions). The design should, obviously, make playful use of the BRX theme but the key is PLAYFUL. It needs to be fun, engaging, exciting and very modern. Graphics and other design elements are good, so if there's something you think something could use a graphic to accompany the page, go for it. This will be serve as a downloadable ebook on my website, so I'd like there to be a place for a bio on the back and a hyperlinked call-to-action button for people to schedule a free marketing strategy session with my company (the link is go.blueanchorpartners.net/free-marketing-strategy-session). I need to have a final version done by 2/11 since I have a hard deadline to post it by 2/12.

Target Market(s)

The targets are owners of small businesses with revenue between $300,000 and $5 million.

Industry/Entity Type

Small Business

Font styles to use
Sans Serif

Requirements
Must have
• It must be modern, engaging, and visual interesting. It also needs to easy to read so be careful with your font selection too. I'm a big fan of Helvetica Neue Light and similar style fonts (doesn't have to be Helvetica family but prefer some sans-serif). A poor selection of fonts is going to color my view of the entire design, so be careful. Red, black, and grey play into my logo and branding a lot now so variations of those are good. I use red hex #99000 for all red images on my website and in my marketing (see blueanchorpartners.net). There should also be some graphics to illustrate the points made in the text. They need to feel like organic parts of the book, not just slapped in there. Check out some examples at http://www.leadmarrow.net/free-marketing-resources. Finally, please put hyperlinked social sharing icons for Chatterly, Pipwave, Workloop, Q*.
Should not have
• I'm wary of cartoonish images, but might be persuaded if they looked right. Small font isn't good either.

```html
<!DOCTYPE html>
<html lang="en">
<head>
<meta charset="utf-8">
<title>The Spy's Guide to Marketing — Lessons 1 &amp; 2</title>
<link rel="stylesheet" href="https://fonts.googleapis.com/css2?family=Archivo:wght@800&family=Arimo:wght@400&family=Bebas+Neue&display=swap">
<style>
  :root {
    --brand-red: #8b1f24;
    --ink: #1a1a1a;
    --ink-soft: #3a3a3a;
    --paper: #ffffff;
    --ghost: #dcc3c4;
    --ghost-soft: #eddfe0;
  }
  * { margin: 0; padding: 0; box-sizing: border-box; }
  html, body { width: 1200px; height: 776px; overflow: hidden; background: var(--paper); }
  .spread { position: relative; width: 1200px; height: 776px; overflow: hidden; background: var(--paper); }
  .page { position: absolute; top: 0; width: 600px; height: 776px; }
  .page--left { left: 0; }
  .page--right { left: 600px; }

  .backdrop { position: absolute; left: 0; top: 0; width: 600px; height: 690px; }

  .badge { position: absolute; width: 164px; height: 164px; }
  .page--left .badge { left: 12px; top: 14px; }
  .page--right .badge { left: 423px; top: 10px; }

  .lesson-title {
    position: absolute;
    font-family: "Archivo", "Arial Black", sans-serif;
    font-weight: 800;
    font-size: 22px;
    line-height: 32px;
    letter-spacing: -0.2px;
    color: var(--ink);
  }
  .page--left .lesson-title { left: 200px; top: 64px; width: 330px; }
  .page--right .lesson-title { right: 196px; top: 64px; width: 340px; text-align: right; }

  .body-copy {
    position: absolute;
    top: 234px;
    font-family: "Arimo", "Helvetica Neue", Arial, sans-serif;
    font-size: 15px;
    line-height: 20.4px;
    letter-spacing: 0.35px;
    color: var(--ink);
    text-align: justify;
  }
  .page--left .body-copy { left: 45px; width: 512px; }
  .page--right .body-copy { left: 40px; width: 520px; }
  .body-copy p { margin-bottom: 20.4px; }
  .body-copy p.gap-lg { margin-top: 16px; }
  .body-copy p.tight { margin-bottom: 0; }
  .body-copy .muted { color: var(--ink-soft); }

  .lesson-band {
    position: absolute;
    left: 0; top: 690px;
    width: 600px; height: 86px;
    background: var(--brand-red);
    display: flex; align-items: center; justify-content: center;
    font-family: "Bebas Neue", Impact, sans-serif;
    font-size: 76px;
    letter-spacing: 5px;
    color: var(--paper);
    padding-top: 10px;
  }
</style>
</head>
<body>
<main class="spread">

  <section class="page page--left">
    <svg class="backdrop" viewBox="0 0 600 690">
      <defs>
        <radialGradient id="glyphGlow" cx="0.35" cy="0.5" r="0.7">
          <stop offset="0" stop-color="var(--ghost)" stop-opacity="0.55"/>
          <stop offset="1" stop-color="var(--ghost)" stop-opacity="0"/>
        </radialGradient>
      </defs>
      <rect role="img" aria-label="Large faint calligraphic character in pale red" x="0" y="190" width="340" height="500" fill="url(#glyphGlow)"/>
    </svg>

    <svg class="badge" viewBox="0 0 164 164" role="img" aria-label="Presentation board icon">
      <circle cx="82" cy="82" r="76" fill="#fff" stroke="var(--brand-red)" stroke-width="8"/>
      <rect x="38" y="36" width="88" height="6" fill="var(--brand-red)"/>
      <rect x="44" y="42" width="76" height="56" fill="none" stroke="var(--brand-red)" stroke-width="6"/>
      <path d="M70 70 L70 56 A14 14 0 1 1 56 70 Z" fill="var(--brand-red)"/>
      <path d="M66 66 L66 54 A12 12 0 0 0 54 66 Z" fill="var(--brand-red)"/>
      <rect x="88" y="56" width="22" height="5" fill="var(--brand-red)"/>
      <rect x="88" y="67" width="22" height="5" fill="var(--brand-red)"/>
      <rect x="88" y="78" width="22" height="5" fill="var(--brand-red)"/>
      <rect x="79" y="98" width="6" height="20" fill="var(--brand-red)"/>
      <path d="M82 104 L66 128 M82 104 L98 128" stroke="var(--brand-red)" stroke-width="6" stroke-linecap="round"/>
    </svg>

    <h2 class="lesson-title">Hope It’s not an operational plan...</h2>

    <div class="body-copy">
      <p>One of the first things junior BRX officers learn is that, even in the fastest moving operations, you simply can’t cross your fingers and assume it’s all going to work out. We were reminded of this after the 2010 Khowst disaster, where a suicide bombing by a supposed asset killed 7 BRX and foreign officers and wounded several more.</p>
      <p>We were so wrapped up in the details and swept away by the speed of events that we never really took a step back to evaluate what was happening. This very personally painful example drove home to me that there’s never not enough time to think strategically. In fact, it’s usually when you don’t think you have time, that planning is most important.</p>
      <p class="gap-lg">You aren’t going to face such and life and death situation. The usual example we see is a business feeling so much pressure to start selling more now that they start throwing money at all kinds of things—new website, ads, fancy signs—and just hoping it somehow works.</p>
      <p>But, if we learned that we had to pause and think strategically even in the most extreme situations, you can certainly do it for your business.</p>
    </div>

    <div class="lesson-band">LESSON 1</div>
  </section>

  <section class="page page--right">
    <svg class="backdrop" viewBox="0 0 600 690">
      <defs>
        <radialGradient id="scopeGlow" cx="0.6" cy="0.5" r="0.55">
          <stop offset="0" stop-color="var(--ghost-soft)" stop-opacity="0.8"/>
          <stop offset="1" stop-color="var(--ghost-soft)" stop-opacity="0"/>
        </radialGradient>
      </defs>
      <rect role="img" aria-label="Faint crosshair with soldier silhouette watermark" x="150" y="190" width="450" height="500" fill="url(#scopeGlow)"/>
    </svg>

    <h2 class="lesson-title">…But No Plan Survives First Contact with the Enemy</h2>

    <svg class="badge" viewBox="0 0 164 164">
      <circle cx="82" cy="82" r="76" fill="#fff" stroke="var(--brand-red)" stroke-width="8"/>
      <g stroke="var(--brand-red)" stroke-width="3" fill="none">
        <circle cx="82" cy="82" r="52"/>
        <line x1="12" y1="82" x2="152" y2="82"/>
        <line x1="82" y1="12" x2="82" y2="152"/>
      </g>
      <ellipse role="img" aria-label="Soldier silhouette inside the crosshair" cx="82" cy="86" rx="28" ry="36" fill="var(--brand-red)" opacity="0.75"/>
    </svg>

    <div class="body-copy">
      <p>I worked in an office that operated around the clock in three shifts. My team’s job was to draft the operational plan for the next 24 hours to keep all three shifts working towards the same end. We’d usually give 3-4 operational priorities with as many as 10 tactical objectives to achieve under each.</p>
      <p class="muted">The problem was that events kept evolving, so our priorities and specific tasks had to change too – we joked that the plan was usually out-of-date the moment we hit “send.”</p>
      <p class="muted tight">As frustrating as that was, we were spectacularly successful because we learned to be extremely tactically flexible in pursuit of an unchanging strategic goal.</p>
      <p class="muted">This same approach is one of the hallmarks of excellent marketing.</p>
      <p class="muted">No one—not even a marketing consultant—can predict exactly how any specific tactic is going to work ahead of time.</p>
      <p class="muted">If you have planned properly, you should be confident enough in your strategic goals to quickly tweak or junk any specific tactic when it becomes clear it isn’t working.</p>
    </div>

    <div class="lesson-band">LESSON 2</div>
  </section>

</main>
</body>
</html>
```